Velmora Partners Logo and Business Card Design

We already have the rough logo shape (however please make the lines on the logo much thicker so a dark background is not required to see it) . see photos uploaded.
It needs to be refined with color and digitized and then have a front and back business card layout done.
The services are high vibration healing support through a therapy and feng shui service offering. We want people to Feel Happiness, Feel Prosperity and Feel Peace. (the back of the card would have these phrases on it) So a warm, calm and peaceful feeling card.
We would like the card to use the logo provided (with thicker lines and color added) but below the graphic please use the name "Velmora Partners" NOT Velmora.
We also would like to use the colors in the colorized matrix shown in photos (gold and purple) but on the lighter side. Thanks for your time!

Front of Card should include: Logo, with Company Name: Velmora Partners as part of logo, Name: Dara Pemberton email: dara@velmora-example.me web: www.velmora-example.me mobile: 555.218.4096 at bottom of front list Family Constellation | Feng Shui

Back of Card should have the logo and the following listed vertically:

PERSONAL | BUSINESS (Larger size then smaller bullet items below)
*Find Happiness
*Find Prosperity
*Find Peace

Target Market(s)

Target market is both business and personal

Contact Information for Business Card

Front of Card should include: Logo, with Company Name: Velmora Partners as part of logo, Name: Dara Pemberton email: dara@velmora-example.me web: www.velmora-example.me mobile: 555.218.4096 at bottom of front list Family Constellation | Feng Shui ++++ Back of Card should have the logo and the following listed vertically: PERSONAL | BUSINESS (Larger size then smaller bullet items below) *Find Happiness *Find Prosperity *Find Peace

Font styles to use
Sans Serif

Colors

Designer to choose colors to be used in the design.

Requirements
Nice to have
• Nice light contrast color for the back of card background
Should not have
• No dark colored background on Card.

```html
<!DOCTYPE html>
<html lang="en">
<head>
<meta charset="utf-8">
<title>Velmora Partners – Business Card</title>
<link rel="stylesheet" href="https://fonts.googleapis.com/css2?family=Raleway:wght@500;700&family=Arimo:wght@400;700&display=swap">
<style>
  :root {
    --page: #2a2a2a;
    --paper: #f7f7f5;
    --olive: #837b00;
    --olive-text: #8a8200;
    --gold-light: #e6dfa3;
    --gold-deep: #5e5800;
    --purple: #4b1590;
    --ink: #000000;
    --white: #ffffff;
    --rule: #9a9a9a;
  }
  * { box-sizing: border-box; margin: 0; padding: 0; }
  html, body {
    width: 1200px; height: 900px; overflow: hidden;
    background: var(--page);
  }
  .canvas {
    width: 1200px; height: 900px;
    display: flex; flex-direction: column; align-items: center; justify-content: center;
    gap: 30px;
  }
  .card {
    position: relative;
    width: 700px; height: 400px;
    overflow: hidden;
    box-shadow: 0 10px 30px rgba(0,0,0,.45);
  }

  /* Front */
  .card--front { background: var(--paper); }
  .brand {
    position: absolute; left: 40px; top: 70px; width: 290px;
    display: flex; flex-direction: column; align-items: center; gap: 22px;
  }
  .brand__dot {
    width: 110px; height: 110px; border-radius: 50%;
    border: 6px solid var(--purple);
  }
  .brand__name {
    font-family: "Raleway", sans-serif; font-weight: 700;
    font-size: 34px; color: var(--ink); white-space: nowrap;
  }
  .divider {
    position: absolute; left: 345px; top: 92px; width: 1px; height: 120px;
    background: var(--rule);
  }
  .contact {
    position: absolute; left: 372px; top: 88px;
    font-family: "Arimo", sans-serif;
  }
  .contact__name {
    font-family: "Raleway", sans-serif; font-weight: 500;
    font-size: 30px; color: var(--olive-text); margin-bottom: 8px;
  }
  .contact__list { list-style: none; }
  .contact__item {
    display: flex; align-items: center; gap: 10px;
    font-size: 17px; color: var(--purple); line-height: 26px;
  }
  .contact__icon { width: 16px; height: 16px; flex: none; }
  .services-band {
    position: absolute; left: 0; right: 0; top: 282px; height: 66px;
    background: var(--ink);
    display: flex; align-items: center; justify-content: center;
    font-family: "Arimo", sans-serif; font-size: 20px; color: var(--olive-text);
  }
  .services-band .sep { color: var(--purple); margin: 0 8px; }

  /* Back */
  .card--back { background: var(--gold-light); }
  .back-brand {
    position: absolute; left: 0; right: 0; top: 26px;
    display: flex; flex-direction: column; align-items: center; gap: 12px;
  }
  .back-brand .brand__dot { width: 86px; height: 86px; border-color: var(--purple); }
  .back-brand .brand__name { font-size: 32px; color: var(--ink); }
  .audience-band {
    position: absolute; left: 0; right: 0; top: 196px; height: 50px;
    background: var(--ink);
    display: flex; align-items: center; justify-content: center;
    font-family: "Arimo", sans-serif; font-weight: 700;
    font-size: 24px; color: var(--white); letter-spacing: .5px;
  }
  .promises {
    position: absolute; left: 0; right: 0; top: 264px;
    display: flex; flex-direction: column; align-items: center;
    list-style: none;
    font-family: "Arimo", sans-serif; font-size: 18px; line-height: 34px;
    color: var(--gold-deep);
  }
</style>
</head>
<body>
<main class="canvas">

  <section class="card card--front" aria-label="Business card front">
    <div class="brand">
      <span class="brand__dot" aria-hidden="true"></span>
      <span class="brand__name">Velmora Partners</span>
    </div>
    <span class="divider" aria-hidden="true"></span>
    <div class="contact">
      <p class="contact__name">Dara Pemberton</p>
      <ul class="contact__list">
        <li class="contact__item">
          <svg class="contact__icon" viewBox="0 0 16 16" aria-hidden="true"><path d="M3 1.5l2.6 0 1.2 3.2-1.6 1.2c.8 1.8 2.2 3.2 4 4l1.2-1.6 3.2 1.2v2.6c0 .8-.7 1.4-1.5 1.4C6.6 13.5 2.5 9.4 1.6 3c0-.8.6-1.5 1.4-1.5z" fill="#837b00"/></svg>
          555.218.4096
        </li>
        <li class="contact__item">
          <svg class="contact__icon" viewBox="0 0 16 16" aria-hidden="true"><rect x="1" y="3" width="14" height="10" fill="#837b00"/><path d="M1 3l7 6 7-6" fill="none" stroke="#f7f7f5" stroke-width="1.2"/></svg>
          dara@velmora-example.me
        </li>
        <li class="contact__item">
          <svg class="contact__icon" viewBox="0 0 16 16" aria-hidden="true"><g fill="none" stroke="#837b00" stroke-width="1.4"><circle cx="8" cy="8" r="6.5"/><ellipse cx="8" cy="8" rx="3" ry="6.5"/><path d="M1.5 8h13M2.5 4.8h11M2.5 11.2h11"/></g></svg>
          www.velmora-example.me
        </li>
      </ul>
    </div>
    <div class="services-band">Family Constellation<span class="sep">|</span>Feng Shui</div>
  </section>

  <section class="card card--back" aria-label="Business card back">
    <div class="back-brand">
      <span class="brand__dot" aria-hidden="true"></span>
      <span class="brand__name">Velmora Partners</span>
    </div>
    <div class="audience-band">PERSONAL | BUSINESS</div>
    <ul class="promises">
      <li>*Find Happiness</li>
      <li>*Find Prosperity</li>
      <li>*Find Peace</li>
    </ul>
  </section>

</main>
</body>
</html>
```